Rate sheet redesign

We provide rate sheets to agents for our scenic flights and I would like to make them easier to read and more comprehensive. I'd also like to be able to edit the information in the design, as tours get updated and so do the rates. We've got new product out of shark bay, so the sections would need to be: Perth, Geraldton, Kalbarri and Shark Bay. I've attached what we've been using and also some concept photos.

also a link to our flights online: https://coralwingtours.bookvista.com/catalog/418752/flights-from-perth

I've put this under brochure redesign as I wasn't sure what a rate sheet would be considered. Open to different formats if it means content is editable.

Need extra days to review

```html
<!DOCTYPE html>
<html lang="en">
<head>
<meta charset="UTF-8">
<title>Pink Lake Schedule and Rates</title>
<link href="https://fonts.googleapis.com/css2?family=Roboto:wght@400;500;700&display=swap" rel="stylesheet">
<style>
  :root {
    --brand-blue: #0b5a9e;
    --brand-orange: #ef9a2a;
    --row-tint: #fde8ce;
    --row-line: #f3d9a4;
    --card: #fbfaf9;
    --ink: #222222;
    --muted: #8a8a8a;
    --white: #ffffff;
  }
  html, body {
    margin: 0;
    padding: 0;
    width: 1200px;
    height: 927px;
    overflow: hidden;
  }
  body {
    position: relative;
    font-family: "Roboto", Arial, sans-serif;
    color: var(--ink);
  }
  .scenery {
    position: absolute;
    inset: 0;
    background:
      linear-gradient(180deg, rgba(255,255,255,0.95) 0%, rgba(246,238,246,0.6) 18%, rgba(230,200,220,0) 35%),
      linear-gradient(90deg, #6d5a60 0%, #c49aa8 10%, #f1dde8 30%, #f6eef4 70%, #c7a3ad 90%, #6f5d62 100%),
      #d9b3c0;
  }
  .scenery::after {
    content: "";
    position: absolute;
    left: 0; right: 0; bottom: 0;
    height: 260px;
    background: linear-gradient(180deg, rgba(196,120,140,0) 0%, #b07080 40%, #6e4e5c 100%);
  }
  .sheet {
    position: absolute;
    left: 108px;
    top: 177px;
    width: 984px;
    height: 614px;
    background: var(--card);
    border-radius: 8px;
  }
  .title-banner {
    position: absolute;
    left: 131px;
    top: 201px;
    width: 432px;
    height: 44px;
  }
  .title-banner svg { position: absolute; inset: 0; }
  .title-banner h1 {
    position: absolute;
    left: 35px;
    top: 0;
    margin: 0;
    line-height: 44px;
    font-size: 29px;
    font-weight: 700;
    color: var(--white);
    letter-spacing: -0.2px;
  }
  .brand {
    position: absolute;
    left: 834px;
    top: 186px;
    width: 232px;
    height: 56px;
    display: flex;
    align-items: center;
    justify-content: flex-end;
    gap: 10px;
  }
  .brand-dot {
    width: 24px;
    height: 24px;
    border-radius: 50%;
    background: var(--brand-blue);
    flex: none;
  }
  .brand-name {
    font-size: 22px;
    font-weight: 500;
    color: var(--brand-blue);
    white-space: nowrap;
  }
  .schedule {
    position: absolute;
    left: 132px;
    top: 265px;
    width: 935px;
  }
  .schedule-head, .schedule-row {
    display: grid;
    grid-template-columns: 176px 292px 292px 175px;
  }
  .schedule-head {
    height: 42px;
    margin-bottom: 5px;
    border: 1.5px solid var(--brand-orange);
    box-sizing: border-box;
  }
  .schedule-head div {
    display: flex;
    align-items: center;
    justify-content: center;
    font-size: 17px;
    font-weight: 700;
  }
  .head-tint { background: var(--brand-orange); color: var(--white); }
  .head-plain { background: var(--white); color: var(--brand-blue); }
  .schedule-row {
    height: 40px;
    margin-bottom: 5px;
    border: 1px solid var(--row-line);
    box-sizing: border-box;
  }
  .schedule-row div {
    display: flex;
    align-items: center;
    justify-content: center;
    font-size: 13.5px;
    white-space: nowrap;
  }
  .col-tint { background: var(--row-tint); }
  .col-plain { background: var(--white); }
  .col-empty { color: var(--muted); }
  .rate-row div { font-weight: 700; color: var(--brand-blue); }
  .rate-row .col-tint { color: var(--ink); }
</style>
</head>
<body>
  <div class="scenery" role="img" aria-label="Photograph of a pink salt lake at dusk with rocky hills reflected in the water"></div>

  <section class="sheet"></section>

  <div class="title-banner">
    <svg width="432" height="44" viewBox="0 0 432 44" aria-hidden="true">
      <polygon points="0,0 396,0 430,44 0,44" fill="var(--brand-orange)"/>
      <polygon points="0,0 368,0 402,44 0,44" fill="var(--brand-blue)"/>
    </svg>
    <h1>PINK LAKE SCHEDULE</h1>
  </div>

  <div class="brand">
    <span class="brand-dot"></span>
    <span class="brand-name">Coralwing Aviation</span>
  </div>

  <div class="schedule">
    <div class="schedule-head">
      <div class="head-plain">PERTH</div>
      <div class="head-tint">GERALDTON</div>
      <div class="head-plain">KALBARRI</div>
      <div class="head-tint">SHARK BAY</div>
    </div>
    <div class="schedule-row"><div class="col-plain col-empty">TBA</div><div class="col-tint">8AM</div><div class="col-plain">8AM</div><div class="col-tint col-empty">TBA</div></div>
    <div class="schedule-row"><div class="col-plain col-empty">TBA</div><div class="col-tint">9:30AM</div><div class="col-plain">9:15AM</div><div class="col-tint col-empty">TBA</div></div>
    <div class="schedule-row"><div class="col-plain col-empty">TBA</div><div class="col-tint">11AM</div><div class="col-plain">10:30AM</div><div class="col-tint col-empty">TBA</div></div>
    <div class="schedule-row"><div class="col-plain col-empty">TBA</div><div class="col-tint">1PM</div><div class="col-plain">11:45AM</div><div class="col-tint col-empty">TBA</div></div>
    <div class="schedule-row"><div class="col-plain col-empty">TBA</div><div class="col-tint">2:30PM</div><div class="col-plain">1:30PM</div><div class="col-tint col-empty">TBA</div></div>
    <div class="schedule-row"><div class="col-plain col-empty">TBA</div><div class="col-tint">4PM</div><div class="col-plain">2:45PM</div><div class="col-tint col-empty">TBA</div></div>
    <div class="schedule-row"><div class="col-plain col-empty">TBA</div><div class="col-tint">5:30PM (NOVEMBER - FEBRUARY ONLY)</div><div class="col-plain">4PM</div><div class="col-tint col-empty">TBA</div></div>
    <div class="schedule-row"><div class="col-plain col-empty">TBA</div><div class="col-tint">6:45PM (DECEMBER AND JANUARY ONLY)</div><div class="col-plain">5:30PM (NOVEMBER - FEBRUARY ONLY)</div><div class="col-tint col-empty">TBA</div></div>
    <div class="schedule-row"><div class="col-plain col-empty">TBA</div><div class="col-tint">END OF SESSIONS</div><div class="col-plain">6:45PM (DECEMBER AND JANUARY ONLY)</div><div class="col-tint col-empty">TBA</div></div>
    <div class="schedule-row rate-row"><div class="col-plain">RATE: $ TBA</div><div class="col-tint">RATE: $ TBA</div><div class="col-plain">RATE: $ TBA</div><div class="col-tint">RATE: $ TBA</div></div>
  </div>
</body>
</html>
```